Harlow Crest Holdings (Remodeling company) needs a logo and business card

We need a business card design for a new company. We "flip" upmarket houses (buy, remodel and sell) in the Austin, TX area. I'd like neutral colors (grey, white, gold black). I would like it to include a simple, clean logo. Our designs are modern and uncluttered and I would like that reflected in the business card design.

Target Market(s)

Young professionals, Families, Retirees. Our properties will sell for $750k+

Industry/Entity Type

Real Estate

Contact Information for Business Card

Harlow Crets Holdings
Mona Harlow
(979) 555 0142
Owner
Rolf Tandem
(512) 555 0176
Realtor

Logo Text

Harlow Crest Holdings

Font styles to use
Serif
Script

Requirements
Must have
• Simple, classic design
Nice to have
• Clean lines, modern look
Should not have
• Too traditionally

```html
<!DOCTYPE html>
<html lang="en">
<head>
<meta charset="utf-8">
<title>Harlow Crest Holdings — Business Card</title>
<link rel="stylesheet" href="https://fonts.googleapis.com/css2?family=Lato:wght@300;400;700&display=swap">
<style>
  :root {
    --page-bg: #e9e6e1;
    --card-dark: #262a33;
    --card-seam: #1b1e25;
    --card-white: #f7f7f5;
    --gold: #f0a020;
    --text-light: #ffffff;
    --text-muted: #b9bcc3;
    --text-owner-muted: #fff3dc;
    --text-dark: #262a33;
  }
  * { box-sizing: border-box; margin: 0; padding: 0; }
  html, body {
    width: 1200px;
    height: 800px;
    overflow: hidden;
    background: var(--page-bg);
    font-family: "Lato", sans-serif;
  }
  .stage {
    width: 1200px;
    height: 800px;
    display: flex;
    align-items: center;
    justify-content: center;
  }
  .business-card {
    width: 840px;
    height: 480px;
    border-radius: 16px;
    overflow: hidden;
    background: var(--card-seam);
    display: grid;
    grid-template-columns: 1fr 1fr;
    grid-template-rows: 1fr 1fr;
    gap: 4px;
    box-shadow: 0 10px 30px rgba(0, 0, 0, 0.18);
  }
  .panel { position: relative; }
  .panel--blank { background: var(--card-dark); }
  .panel--brand {
    background: var(--card-white);
    display: flex;
    align-items: center;
    justify-content: center;
  }
  .panel--owner { background: var(--gold); }
  .panel--realtor { background: var(--card-dark); }

  .brand {
    display: flex;
    align-items: center;
    gap: 16px;
  }
  .brand-mark {
    width: 18px;
    height: 18px;
    background: var(--gold);
    flex: none;
  }
  .brand-name {
    font-weight: 700;
    font-size: 36px;
    line-height: 1.05;
    letter-spacing: 1px;
    text-transform: uppercase;
    color: var(--text-dark);
  }

  .contact {
    position: absolute;
    left: 48px;
    top: 62px;
  }
  .contact-name {
    font-weight: 400;
    font-size: 30px;
    letter-spacing: 0.5px;
    text-transform: uppercase;
    color: var(--text-light);
  }
  .contact-role {
    font-weight: 300;
    font-size: 20px;
    margin-left: 6px;
    margin-top: 2px;
  }
  .panel--owner .contact-role { color: var(--text-owner-muted); }
  .panel--realtor .contact-role { color: var(--text-muted); }
  .contact-phone {
    display: flex;
    align-items: center;
    gap: 18px;
    margin-top: 20px;
    margin-left: 10px;
    font-size: 17px;
    letter-spacing: 0.5px;
    color: var(--text-light);
  }
  .phone-icon { width: 22px; height: 30px; flex: none; }
</style>
</head>
<body>
  <main class="stage">
    <article class="business-card">
      <div class="panel panel--blank"></div>

      <div class="panel panel--brand">
        <div class="brand">
          <span class="brand-mark"></span>
          <span class="brand-name">Harlow Crest<br>Holdings</span>
        </div>
      </div>

      <div class="panel panel--owner">
        <div class="contact">
          <p class="contact-name">Mona Harlow</p>
          <p class="contact-role">Owner</p>
          <p class="contact-phone">
            <svg class="phone-icon" viewBox="0 0 22 30" aria-hidden="true">
              <rect x="1" y="1" width="20" height="28" rx="4" fill="#ffffff"/>
              <rect x="4.5" y="4.5" width="13" height="9" rx="1" fill="#f0a020"/>
              <g fill="#f0a020">
                <rect x="5" y="17" width="3" height="2.5"/><rect x="9.5" y="17" width="3" height="2.5"/><rect x="14" y="17" width="3" height="2.5"/>
                <rect x="5" y="21.5" width="3" height="2.5"/><rect x="9.5" y="21.5" width="3" height="2.5"/><rect x="14" y="21.5" width="3" height="2.5"/>
              </g>
            </svg>
            (979) 555 0142
          </p>
        </div>
      </div>

      <div class="panel panel--realtor">
        <div class="contact">
          <p class="contact-name">Rolf Tandem</p>
          <p class="contact-role">Realtor</p>
          <p class="contact-phone">
            <svg class="phone-icon" viewBox="0 0 22 30" aria-hidden="true">
              <rect x="1" y="1" width="20" height="28" rx="4" fill="#ffffff"/>
              <rect x="4.5" y="4.5" width="13" height="9" rx="1" fill="#262a33"/>
              <g fill="#262a33">
                <rect x="5" y="17" width="3" height="2.5"/><rect x="9.5" y="17" width="3" height="2.5"/><rect x="14" y="17" width="3" height="2.5"/>
                <rect x="5" y="21.5" width="3" height="2.5"/><rect x="9.5" y="21.5" width="3" height="2.5"/><rect x="14" y="21.5" width="3" height="2.5"/>
              </g>
            </svg>
            (512) 555 0176
          </p>
        </div>
      </div>
    </article>
  </main>
</body>
</html>
```